Bref créative
Modern Creative Stationary for Tech Start up!!!
TheByteDepot - Business cards - Letterheads - Email Signature -
Use same font as used in my logo
Smaller Text can be different- but in line with theme.
Professional
Pavel Orsk
Sales & Logistics
3rd Floor Birch Court
7X Fernhill Street
Harrow
London
HBX 8QW
0208 731 XXXX
07452168XXX
pavel@thebytedepotz.com
thebytedepotz.com
We want a double sided Business card that is elegant, modern, sleek and also creative. The logo should give you an idea of where we want to go in terms of theme.
Be creative, Be sexy and try your hardest as there is plenty more work to be done after this project.
This is our Logo.
We do not really like the shaded background. So it might be best to keep it flat black.
This is the white version of our Logo. It may be an idea to use this for the stationary.

```html
<!DOCTYPE html>
<html lang="en">
<head>
<meta charset="utf-8">
<title>TheByteDepot Stationery</title>
<link rel="stylesheet" href="https://fonts.googleapis.com/css2?family=Exo+2:wght@700&family=Open+Sans:wght@400;600;700&display=swap">
<style>
  :root {
    --bg: #eceef0;
    --paper: #ffffff;
    --ink: #2b2b2b;
    --muted: #8a8d91;
    --rule: #d4d6d9;
    --band: #c9cbce;
    --card-black: #141414;
    --accent: #2e9fd8;
  }
  * { box-sizing: border-box; margin: 0; padding: 0; }
  html, body { width: 1200px; height: 794px; overflow: hidden; }
  body { background: var(--bg); font-family: "Open Sans", Arial, sans-serif; color: var(--ink); position: relative; }

  .sheet, .card, .envelope { position: absolute; box-shadow: 0 6px 18px rgba(0,0,0,0.12); }

  .brand { display: flex; align-items: center; gap: 4px; font-family: "Exo 2", "Arial Black", sans-serif; font-weight: 700; color: var(--ink); letter-spacing: 0.2px; white-space: nowrap; }
  .brand-dot { width: 9px; height: 9px; border-radius: 50%; background: var(--accent); flex: none; }
  .brand--light { color: #ffffff; }

  /* Letterhead */
  .letterhead { left: 370px; top: 30px; width: 300px; height: 424px; background: var(--paper); padding: 22px 26px; font-size: 4.6px; line-height: 1.55; }
  .letterhead .brand { font-size: 12px; }
  .sender-address { position: absolute; right: 26px; top: 22px; text-align: right; color: var(--muted); font-size: 4.4px; line-height: 1.5; font-style: normal; }
  .recipient { margin-top: 30px; }
  .letter-date { margin-top: 10px; }
  .salutation { margin-top: 10px; }
  .letter-body p { margin-top: 6px; max-width: 230px; }
  .signature { margin-top: 12px; width: 52px; height: 12px; background: linear-gradient(90deg, #cfd2d6, #e9eaec); border-radius: 2px; }
  .signatory { margin-top: 4px; font-weight: 600; }

  /* Fax */
  .fax { left: 730px; top: 30px; width: 300px; height: 424px; background: var(--paper); padding: 22px 26px; font-size: 4.8px; }
  .fax .brand { font-size: 12px; }
  .fax-title { position: absolute; right: 26px; top: 104px; font-size: 15px; font-weight: 700; letter-spacing: 1px; color: #333; }
  .fax-fields { position: absolute; left: 26px; top: 70px; width: 170px; }
  .fax-field { display: flex; border-bottom: 0.6px solid var(--rule); height: 11px; align-items: flex-end; padding-bottom: 1px; }
  .fax-field span { width: 28px; font-weight: 600; }
  .fax-band { position: absolute; left: 26px; right: 26px; top: 160px; height: 7px; background: var(--band); }
  .fax-checks { position: absolute; left: 26px; right: 26px; top: 174px; display: flex; justify-content: space-between; }
  .fax-check { display: flex; align-items: center; gap: 2px; }
  .fax-check i { width: 4px; height: 4px; border: 0.6px solid #777; display: block; }
  .fax-comments { position: absolute; left: 26px; top: 190px; font-weight: 600; }

  /* Business cards */
  .card { width: 220px; height: 126px; background: var(--card-black); color: #fff; overflow: hidden; }
  .card-logo { left: 110px; top: 70px; }
  .card-logo .brand { position: absolute; left: 18px; top: 20px; font-size: 14px; }
  .card-contact { left: 110px; top: 216px; padding: 16px 18px; font-size: 5px; line-height: 1.6; color: #d8d8d8; }
  .card-contact .brand { font-size: 10px; margin-bottom: 8px; }
  .card-name { font-size: 7px; font-weight: 700; color: #fff; }
  .card-role { color: var(--muted); margin-bottom: 5px; }

  /* Envelopes */
  .envelope { width: 330px; height: 160px; background: var(--paper); }
  .envelope-front { left: 370px; top: 520px; padding: 18px 22px; }
  .envelope-front .brand { font-size: 12px; }
  .envelope-window { position: absolute; left: 170px; top: 44px; width: 120px; height: 38px; border: 0.8px solid var(--rule); border-radius: 3px; }
  .envelope-back { left: 730px; top: 520px; overflow: hidden; }
  .envelope-back svg { position: absolute; inset: 0; }
  .envelope-back .brand { position: absolute; left: 50%; top: 52px; transform: translateX(-50%); font-size: 9px; }
</style>
</head>
<body>

  <section class="sheet letterhead">
    <div class="brand"><span class="brand-dot"></span>TheByteDepot</div>
    <address class="sender-address">
      3rd Floor Birch Court<br>7X Fernhill Street<br>Harrow, London<br>HBX 8QW<br>0208 731 XXXX<br>thebytedepotz.com
    </address>
    <div class="recipient">Recipient Name<br>Company Address<br>City, Postcode</div>
    <div class="letter-date">12 March 2024</div>
    <div class="salutation">Dear Sir,</div>
    <div class="letter-body">
      <p>Thank you for your recent enquiry about our hardware and logistics services. We are pleased to confirm that your order has been received and is now being prepared for dispatch.</p>
      <p>Our team will contact you within two working days to arrange delivery at a time that suits you best.</p>
      <p>Please do not hesitate to get in touch should you have any further questions.</p>
      <p>Kind regards,</p>
    </div>
    <div class="signature" role="img" aria-label="Handwritten signature"></div>
    <div class="signatory">Pavel Orsk</div>
    <div>Sales &amp; Logistics</div>
  </section>

  <section class="sheet fax">
    <div class="brand"><span class="brand-dot"></span>TheByteDepot</div>
    <address class="sender-address">
      3rd Floor Birch Court<br>7X Fernhill Street<br>Harrow, London<br>HBX 8QW<br>0208 731 XXXX
    </address>
    <div class="fax-fields">
      <div class="fax-field"><span>To:</span></div>
      <div class="fax-field"><span>From:</span></div>
      <div class="fax-field"><span>Fax:</span></div>
      <div class="fax-field"><span>Pages:</span></div>
      <div class="fax-field"><span>Phone:</span></div>
      <div class="fax-field"><span>Date:</span></div>
      <div class="fax-field"><span>Re:</span></div>
      <div class="fax-field"><span>CC:</span></div>
    </div>
    <div class="fax-title">FAX</div>
    <div class="fax-band"></div>
    <div class="fax-checks">
      <div class="fax-check"><i></i>Urgent</div>
      <div class="fax-check"><i></i>For Review</div>
      <div class="fax-check"><i></i>Please Comment</div>
      <div class="fax-check"><i></i>Please Reply</div>
      <div class="fax-check"><i></i>Please Recycle</div>
    </div>
    <div class="fax-comments">Comments:</div>
  </section>

  <section class="card card-logo">
    <div class="brand brand--light"><span class="brand-dot"></span>TheByteDepot</div>
  </section>

  <section class="card card-contact">
    <div class="brand brand--light"><span class="brand-dot"></span>TheByteDepot</div>
    <div class="card-name">Pavel Orsk</div>
    <div class="card-role">Sales &amp; Logistics</div>
    <div>T: 0208 731 XXXX &nbsp; M: 07452168XXX</div>
    <div>pavel@thebytedepotz.com</div>
    <div>thebytedepotz.com</div>
  </section>

  <section class="envelope envelope-front">
    <div class="brand"><span class="brand-dot"></span>TheByteDepot</div>
    <div class="envelope-window"></div>
  </section>

  <section class="envelope envelope-back">
    <svg width="330" height="160" viewBox="0 0 330 160" aria-hidden="true">
      <polygon points="0,0 330,0 165,100" fill="var(--card-black)"/>
      <line x1="0" y1="160" x2="150" y2="72" stroke="var(--rule)" stroke-width="0.8"/>
      <line x1="330" y1="160" x2="180" y2="72" stroke="var(--rule)" stroke-width="0.8"/>
    </svg>
    <div class="brand brand--light"><span class="brand-dot"></span>TheByteDepot</div>
  </section>

</body>
</html>
```